Business Card Design Project

Taprilo - based in Melbourne, Australia. We plan, design, implement and support network infrastructure (Vorda, Halvest, K8, Tarnwick etc).

Target Market(s)

Small/Medium enterprise and Corporate.

Industry/Entity Type

Business

```html
<!DOCTYPE html>
<html lang="en">
<head>
<meta charset="utf-8">
<title>Taprilo business card</title>
<link href="https://fonts.googleapis.com/css2?family=Questrial&family=Open+Sans:wght@400;600&display=swap" rel="stylesheet">
<style>
  :root{
    --canvas:#e9e7e3;
    --paper:#ffffff;
    --orange:#e0802b;
    --grey:#646568;
    --grey-light:#b9babc;
    --text:#5a5b5e;
    --dark:#2f2f31;
    --dark-soft:#3a3a3c;
    --white:#ffffff;
  }
  *{box-sizing:border-box;margin:0;padding:0}
  html,body{width:1200px;height:858px;overflow:hidden;background:var(--canvas)}
  .stage{position:relative;width:1200px;height:858px;display:flex;align-items:center;justify-content:center;gap:50px}
  .card{position:relative;width:530px;height:303px;overflow:hidden;box-shadow:0 8px 22px rgba(0,0,0,.18)}

  /* front */
  .card--front{background:var(--paper)}
  .brand{position:absolute;left:40px;top:56px;display:flex;align-items:center;gap:14px}
  .brand__dot{width:46px;height:46px;border-radius:50%;background:var(--grey)}
  .brand__name{font-family:'Questrial',sans-serif;font-size:72px;line-height:1;color:var(--orange);letter-spacing:-1px}
  .person{position:absolute;left:44px;top:190px}
  .person__name{font-family:'Questrial',sans-serif;font-size:24px;color:var(--orange)}
  .person__role{font-family:'Open Sans',sans-serif;font-size:11px;color:var(--text);margin-top:2px}
  .divider{position:absolute;left:318px;top:34px;width:1px;height:200px;background:var(--grey-light)}
  .contact{position:absolute;left:336px;top:104px;font-family:'Open Sans',sans-serif;font-size:11px;color:var(--text);line-height:1.45}
  .contact__address{margin-bottom:12px}
  .contact__row{display:flex;align-items:center;gap:8px}
  .contact__icon{width:12px;height:12px;flex:none}
  .accent-line{position:absolute;left:0;right:0;bottom:42px;height:2px;background:var(--orange)}
  .band{position:absolute;left:0;right:0;bottom:0;height:38px;background:var(--grey)}

  /* back */
  .card--back{background:var(--dark)}
  .back__brand{position:absolute;left:120px;top:66px;font-family:'Questrial',sans-serif;font-size:82px;line-height:1;color:var(--white);letter-spacing:-1px}
  .back__tagline{position:absolute;left:40px;top:166px;font-family:'Open Sans',sans-serif;font-size:12px;color:var(--white)}
  .back__rule{position:absolute;left:40px;right:40px;top:200px;height:1px;background:rgba(255,255,255,.7)}
  .partners{position:absolute;left:40px;right:40px;top:220px;display:flex;justify-content:space-between;align-items:center}
  .partner{background:var(--white);font-family:'Open Sans',sans-serif;font-weight:600;font-size:13px;color:var(--dark);padding:6px 12px}
</style>
</head>
<body>
<main class="stage">
  <section class="card card--front" aria-label="Card front">
    <div class="brand">
      <span class="brand__dot"></span>
      <span class="brand__name">taprilo</span>
    </div>
    <div class="person">
      <p class="person__name">Employee Name</p>
      <p class="person__role">Managing Director</p>
    </div>
    <div class="divider"></div>
    <div class="contact">
      <p class="contact__address">Address your Inc 00 2nd<br>Ave Harlow, VC xxxxx</p>
      <p class="contact__row">
        <svg class="contact__icon" viewBox="0 0 12 12"><path d="M2 1h3l1 3-2 1a7 7 0 0 0 3 3l1-2 3 1v3c-6 0-9-3-9-9z" fill="var(--orange)"/></svg>
        012 345 6789</p>
      <p class="contact__row">
        <svg class="contact__icon" viewBox="0 0 12 12"><rect x="0.5" y="2" width="11" height="8" fill="var(--orange)"/><path d="M1 2.5l5 4 5-4" stroke="#fff" fill="none"/></svg>
        info@yourwebsite.com</p>
      <p class="contact__row">
        <svg class="contact__icon" viewBox="0 0 12 12"><circle cx="6" cy="6" r="5.5" fill="var(--orange)"/><path d="M0.5 6h11M6 .5c-3 3-3 8 0 11M6 .5c3 3 3 8 0 11" stroke="#fff" stroke-width=".8" fill="none"/></svg>
        www.yourwebsite.com</p>
    </div>
    <div class="accent-line"></div>
    <div class="band"></div>
  </section>

  <section class="card card--back" aria-label="Card back">
    <p class="back__brand">taprilo</p>
    <p class="back__tagline">We plan, design, implement and support network infrastructure</p>
    <div class="back__rule"></div>
    <div class="partners">
      <span class="partner">Vorda</span>
      <span class="partner">Halvest</span>
      <span class="partner">K8</span>
      <span class="partner">Tarnwick</span>
    </div>
  </section>
</main>
</body>
</html>
```